Family Ranch with a hobby vineyard needs 2 wine labels for our first harvest

Design 2 wine labels (front and back) with the Brindor Ranch logo.
Label 1:
Sauvignon Blanc
Alc. 12.5% by Vol.
Palos Verdes Peninsula - add as the region
Year 2022
Label 2:
Cabernet Sauvignon
Alc. 13.5% by Vol.
Year 2022
For the back label design:
GOVERNMENT WARNING: (1) According to the Surgeon General, women
should not drink alcoholic beverages during pregnancy because of the risk of
birth defects. (2) Consumption of alcoholic beverages impairs your ability to
drive a car or operate machinery, and may cause health problems.
Contains Sulfates.
750ML
I just received the bottles and have attached a picture.
Look and feel
Each slider illustrates characteristics of the customer's brand and the style your logo design should communicate.

```html
<!DOCTYPE html>
<html lang="en">
<head>
<meta charset="utf-8">
<title>Brindor Ranch – Wine Labels</title>
<link rel="stylesheet" href="https://fonts.googleapis.com/css2?family=Montserrat:wght@400;500;600&family=Arimo:wght@400;700&display=swap">
<style>
  :root {
    --bg: #dcdde0;
    --label: #ffffff;
    --ink: #3a3a3c;
    --ink-soft: #555558;
    --gold: #b8962e;
    --gold-line: #c9ad5a;
    --accent-cab: #f4c430;
    --accent-blanc: #d9343c;
    --etch-light: #e9e9ea;
    --etch-dark: #bdbdc0;
  }
  * { margin: 0; padding: 0; box-sizing: border-box; }
  html, body { width: 1200px; height: 2700px; overflow: hidden; }
  body {
    background: var(--bg);
    font-family: "Montserrat", sans-serif;
    color: var(--ink);
    position: relative;
  }
  .label {
    position: absolute;
    left: 250px;
    width: 700px;
  }
  .label-front { height: 800px; }
  .label-back { height: 410px; }
  .label-shape {
    position: absolute;
    inset: 0;
    width: 100%;
    height: 100%;
    filter: drop-shadow(0 4px 10px rgba(0,0,0,0.08));
  }
  .label-content {
    position: absolute;
    inset: 0;
    text-align: center;
  }
  .brand {
    position: absolute;
    top: 40px;
    left: 0;
    right: 0;
    display: flex;
    flex-direction: column;
    align-items: center;
    gap: 14px;
  }
  .brand-dot {
    width: 52px;
    height: 52px;
    border-radius: 50%;
    background: var(--gold);
  }
  .brand-name {
    font-family: "Montserrat", sans-serif;
    font-weight: 500;
    font-size: 30px;
    letter-spacing: 3px;
    color: var(--ink);
    text-transform: uppercase;
  }
  .varietal {
    position: absolute;
    top: 212px;
    left: 0;
    right: 0;
    font-weight: 600;
    font-size: 58px;
    line-height: 56px;
    letter-spacing: 4px;
    color: var(--ink);
  }
  .divider {
    position: absolute;
    top: 362px;
    left: 310px;
    width: 80px;
    height: 2px;
    background: var(--gold-line);
  }
  .region {
    position: absolute;
    top: 392px;
    left: 0;
    right: 0;
    font-size: 20px;
    letter-spacing: 4px;
    color: var(--ink-soft);
  }
  .vintage {
    position: absolute;
    top: 432px;
    left: 0;
    right: 0;
    font-size: 24px;
    font-weight: 600;
    letter-spacing: 4px;
    color: var(--ink);
  }
  .abv {
    position: absolute;
    top: 730px;
    left: 0;
    right: 0;
    font-family: "Arimo", sans-serif;
    font-size: 22px;
    letter-spacing: 1px;
    color: var(--ink-soft);
  }
  .warning {
    position: absolute;
    top: 120px;
    left: 52px;
    right: 52px;
    font-family: "Arimo", sans-serif;
    font-size: 19.5px;
    line-height: 24px;
    text-align: justify;
    text-align-last: center;
    color: var(--ink);
  }
  .warning strong { font-weight: 700; letter-spacing: 0.5px; }
  .sulfites, .volume {
    position: absolute;
    left: 0;
    right: 0;
    font-family: "Arimo", sans-serif;
    font-size: 19px;
    color: var(--ink);
  }
  .sulfites { top: 290px; }
  .volume { top: 352px; }
</style>
</head>
<body>

<!-- Sauvignon Blanc front label -->
<section class="label label-front" style="top:115px">
  <svg class="label-shape" viewBox="0 0 700 800" aria-hidden="true">
    <defs>
      <clipPath id="clip-blanc">
        <path d="M0,60 Q0,40 20,36 Q350,-22 680,36 Q700,40 700,60 L700,780 Q700,800 680,800 L20,800 Q0,800 0,780 Z"/>
      </clipPath>
      <linearGradient id="etch-blanc" x1="0" y1="0" x2="0" y2="1">
        <stop offset="0" stop-color="var(--etch-light)"/>
        <stop offset="1" stop-color="var(--etch-dark)"/>
      </linearGradient>
    </defs>
    <g clip-path="url(#clip-blanc)">
      <rect width="700" height="800" fill="var(--label)"/>
      <rect x="0" y="485" width="700" height="220" fill="url(#etch-blanc)" role="img" aria-label="Etched vineyard landscape with rolling hills, trees and vine rows"/>
      <polygon points="470,800 565,800 700,680 700,590" fill="var(--accent-blanc)"/>
    </g>
  </svg>
  <div class="label-content">
    <div class="brand"><span class="brand-dot"></span><span class="brand-name">Brindor Ranch</span></div>
    <h1 class="varietal">SAUVIGNON<br>BLANC</h1>
    <span class="divider"></span>
    <p class="region">PALOS VERDES PENINSULA</p>
    <p class="vintage">2022</p>
    <p class="abv">ALC. 12.5% / VOL.</p>
  </div>
</section>

<!-- Cabernet Sauvignon front label -->
<section class="label label-front" style="top:1015px">
  <svg class="label-shape" viewBox="0 0 700 800" aria-hidden="true">
    <defs>
      <clipPath id="clip-cab">
        <path d="M0,60 Q0,40 20,36 Q350,-22 680,36 Q700,40 700,60 L700,780 Q700,800 680,800 L20,800 Q0,800 0,780 Z"/>
      </clipPath>
      <linearGradient id="etch-cab" x1="0" y1="0" x2="0" y2="1">
        <stop offset="0" stop-color="var(--etch-light)"/>
        <stop offset="1" stop-color="var(--etch-dark)"/>
      </linearGradient>
    </defs>
    <g clip-path="url(#clip-cab)">
      <rect width="700" height="800" fill="var(--label)"/>
      <rect x="0" y="485" width="700" height="220" fill="url(#etch-cab)" role="img" aria-label="Etched vineyard landscape with rolling hills, trees and vine rows"/>
      <polygon points="470,800 565,800 700,680 700,590" fill="var(--accent-cab)"/>
    </g>
  </svg>
  <div class="label-content">
    <div class="brand"><span class="brand-dot"></span><span class="brand-name">Brindor Ranch</span></div>
    <h1 class="varietal">CABERNET<br>SAUVIGNON</h1>
    <span class="divider"></span>
    <p class="region">PALOS VERDES PENINSULA</p>
    <p class="vintage">2022</p>
    <p class="abv">ALC. 13.5% / VOL.</p>
  </div>
</section>

<!-- Cabernet Sauvignon back label -->
<section class="label label-back" style="top:1915px">
  <svg class="label-shape" viewBox="0 0 700 410" aria-hidden="true">
    <defs>
      <clipPath id="clip-back">
        <path d="M0,60 Q0,40 20,36 Q350,-22 680,36 Q700,40 700,60 L700,390 Q700,410 680,410 L20,410 Q0,410 0,390 Z"/>
      </clipPath>
    </defs>
    <g clip-path="url(#clip-back)">
      <rect width="700" height="410" fill="var(--label)"/>
      <polygon points="0,110 125,0 225,0 0,190" fill="var(--accent-cab)"/>
    </g>
  </svg>
  <div class="label-content">
    <p class="warning"><strong>GOVERNMENT WARNING:</strong> (1) According to the Surgeon General, women should not drink alcoholic beverages during pregnancy because of the risk of birth defects. (2) Consumption of alcoholic beverages impairs your ability to drive a car or operate machinery, and may cause health problems.</p>
    <p class="sulfites">Contains Sulfates</p>
    <p class="volume">750ML</p>
  </div>
</section>

</body>
</html>
```